Brand New Africa Focused Specialty Insurance business needs a slick website

Meridane Underwriting Partners needs a slick website design to launch our business with. we have 3 lines of business to begin with - Political Risk and Trade Credit and Property. (this will extend to 9: Political violence and Terrorism, Construction, Liability, Energy, Aviation, Marine, Parametric and Crisis Management at a later date). We are based in London but are Africa focused and our mission statement Meridane Underwriting Partners provides comprehensive, bespoke insurance risk mitigating solutions to local and global customers, giving them the confidence to grow their businesses sustainably. our tagline is "protecting Africa". Our colours are purple (Red 36, Green 11, Blue 96) and gold (Red 143, Green 137, Blue 53).

Target Market(s)

Brokers
Businesses across africa

Coding

Number of Pages Required

4 page

Font styles to use
Sans Serif
Other font styles liked:
• Cairo (but open to others too)

Requirements
Must have
• Pages:
1. Home page/about us (to include Lines of Business)
2. a page for Property line (we will need to add a link so that people can send an email to the mailbox)
3. a page for Political Risk and Trade Credit ( we will need to add a link so that people can send an email to the mailbox)
3. a page about our people (photos not yet taken for this)
4. a careers page
we have a lot of text for the above, we just need to fine tune it

must be tied to the colour scheme I detailed above.

the font for the logo is called Cairo
Nice to have
• https://www.torvalex-mutual.com/ - we like the look of this website, but perhaps less colour
Should not have
• Any African animal like Lions or Zebras

```html
<!DOCTYPE html>
<html lang="en">
<head>
<meta charset="utf-8">
<title>Careers – Meridane Underwriting Partners</title>
<link rel="stylesheet" href="https://fonts.googleapis.com/css2?family=Cairo:wght@400;600;700&display=swap">
<style>
  :root {
    --purple: #240b60;
    --purple-deep: #1a0748;
    --gold: #8f8935;
    --ink: #4a4a55;
    --muted: #8a8796;
    --white: #ffffff;
    --field-line: rgba(255,255,255,0.35);
  }
  * { box-sizing: border-box; margin: 0; padding: 0; }
  html, body { width: 745px; height: 1200px; overflow: hidden; }
  body { font-family: "Cairo", sans-serif; background: var(--white); color: var(--ink); position: relative; }

  /* Header */
  .site-header { position: absolute; top: 0; left: 0; width: 745px; height: 44px; z-index: 3; }
  .brand { position: absolute; left: 52px; top: 0; width: 170px; height: 58px; background: var(--white);
           display: flex; align-items: center; gap: 8px; padding: 0 12px; box-shadow: 0 2px 6px rgba(0,0,0,0.12); }
  .brand-mark { width: 30px; height: 30px; border-radius: 50%; border: 3px solid var(--gold); flex: none; }
  .brand-text { line-height: 1.05; }
  .brand-name { font-weight: 700; font-size: 9.5px; color: var(--purple); display: block; }
  .brand-tagline { font-size: 7px; color: var(--muted); display: block; margin-top: 2px; }
  .main-nav { position: absolute; left: 236px; top: 0; right: 0; height: 44px; background: var(--purple);
              display: flex; align-items: center; gap: 34px; padding-left: 70px; }
  .main-nav a { color: var(--white); text-decoration: none; font-size: 9px; font-weight: 600; letter-spacing: 0.4px; position: relative; }
  .main-nav a.active::after { content: ""; position: absolute; left: 0; right: 0; bottom: -5px; height: 2px; background: var(--gold); }
  .caret { font-size: 7px; margin-left: 3px; }

  /* Hero */
  .hero { position: absolute; top: 0; left: 0; width: 745px; height: 322px; overflow: hidden; }
  .hero-photo { position: absolute; inset: 0;
    background: linear-gradient(180deg, #e6e2ec 0%, #cfc8dc 45%, #8c7fae 78%, #3b2577 100%); }
  .hero-photo::after { content: ""; position: absolute; right: 70px; top: 60px; width: 230px; height: 240px;
    background: radial-gradient(ellipse at center, rgba(143,137,53,0.55) 0%, rgba(143,137,53,0) 70%); }
  .hero-title { position: absolute; left: 72px; top: 212px; color: var(--white); font-size: 34px; font-weight: 700; letter-spacing: 1px; }
  .hero-title::after { content: ""; display: block; width: 52px; height: 3px; background: var(--gold); margin-top: 2px; }

  /* Content */
  .careers-content { position: absolute; top: 355px; left: 72px; width: 610px; }
  .section-title { color: var(--purple); font-size: 21px; font-weight: 700; letter-spacing: 0.5px; }
  .section-title::after { content: ""; display: block; width: 46px; height: 3px; background: var(--gold); margin-top: 1px; }
  .benefit-list { list-style: none; margin-top: 18px; }
  .benefit-list li { position: relative; padding-left: 16px; font-size: 8.4px; line-height: 1.75; margin-bottom: 14px; color: var(--ink); }
  .benefit-list li::before { content: ""; position: absolute; left: 0; top: 4px; width: 6px; height: 6px; border-radius: 50%; background: var(--gold); }

  /* Message */
  .message-section { position: absolute; top: 705px; left: 0; width: 745px; height: 350px; overflow: hidden; }
  .message-backdrop { position: absolute; inset: 0;
    background: linear-gradient(180deg, var(--purple) 0%, #2d1570 55%, #3b2a7a 80%, #2a1566 100%); }
  .message-inner { position: relative; width: 390px; margin: 0 auto; padding-top: 42px; text-align: center; }
  .message-title { color: var(--white); font-size: 22px; font-weight: 600; letter-spacing: 0.6px; }
  .message-title::after { content: ""; display: block; width: 48px; height: 3px; background: var(--gold); margin: 2px auto 0; }
  .message-form { margin-top: 24px; display: grid; grid-template-columns: 1fr 1fr; gap: 9px; text-align: left; }
  .field { border: 1px solid var(--field-line); height: 25px; color: rgba(255,255,255,0.8); font-size: 7.5px; padding: 6px 8px; letter-spacing: 0.4px; }
  .field-wide { grid-column: 1 / 3; }
  .field-message { grid-column: 1 / 3; height: 100px; }
  .send-button { grid-column: 1 / 3; justify-self: center; margin-top: 10px; width: 70px; height: 24px; background: var(--gold);
                 color: var(--white); font-size: 8px; font-weight: 700; letter-spacing: 1px; display: flex; align-items: center; justify-content: center; }

  /* Footer */
  .site-footer { position: absolute; top: 1055px; left: 0; width: 745px; height: 145px; text-align: center; }
  .footer-brand { display: inline-flex; align-items: center; gap: 8px; margin-top: 22px; text-align: left; }
  .footer-nav { display: flex; justify-content: center; gap: 40px; margin-top: 14px; }
  .footer-nav a { color: var(--purple); text-decoration: none; font-size: 8px; font-weight: 700; letter-spacing: 0.4px; }
  .copyright { font-size: 7px; color: var(--muted); margin-top: 8px; }
</style>
</head>
<body>

<header class="site-header">
  <div class="brand">
    <span class="brand-mark"></span>
    <span class="brand-text">
      <span class="brand-name">Meridane Underwriting Partners</span>
      <span class="brand-tagline">Protecting Africa</span>
    </span>
  </div>
  <nav class="main-nav">
    <a href="#">HOME</a>
    <a href="#">ABOUT US</a>
    <a href="#">LINE OF BUSINESS<span class="caret">▾</span></a>
    <a href="#" class="active">CAREER</a>
  </nav>
</header>

<section class="hero">
  <div class="hero-photo" role="img" aria-label="City skyline with a businessman walking towards a large map of Africa, tinted purple"></div>
  <h1 class="hero-title">CAREERS</h1>
</section>

<main class="careers-content">
  <h2 class="section-title">CAREERS</h2>
  <ul class="benefit-list">
    <li>As a new company eager to make a name for ourselves, we understand that collaboration and hard work are key principles to achieving the results we seek.</li>
    <li>Our collaborative approach has the great benefit of fostering a learning environment where we can ensure that our people grow professionally and continually develop their skills and experience – as our business thrives, so should our people. Therefore, we support further studies, whether in the form of professional qualifications, degrees, or related soft skills.</li>
    <li>As well as personal and career development, we want to ensure that our people have the best range of benefits possible. Naturally, this means that financial benefits such as life assurance, pension, and private medical insurance are available; however, we also recognise the need for benefits which promote a healthy work-life balance, flexible working, and mental health support.</li>
    <li>Diversity and inclusion are key values at Meridane, and therefore we recruit from all backgrounds and work hard to ensure that all our people feel included and an inherent part of the team. We are interested in people's skills, ideas and experiences, so if you think that you have what it takes to join our diverse team, please send your CV to careers@meridane-up.com</li>
  </ul>
</main>

<section class="message-section">
  <div class="message-backdrop" role="img" aria-label="Dusk landscape of African trees under a purple sky"></div>
  <div class="message-inner">
    <h2 class="message-title">LEAVE US A MESSAGE</h2>
    <div class="message-form">
      <div class="field">FIRST NAME *</div>
      <div class="field">LAST NAME *</div>
      <div class="field field-wide">E-MAIL *</div>
      <div class="field field-message">YOUR MESSAGE *</div>
      <div class="send-button">SEND</div>
    </div>
  </div>
</section>

<footer class="site-footer">
  <div class="footer-brand">
    <span class="brand-mark"></span>
    <span class="brand-text">
      <span class="brand-name">Meridane Underwriting Partners</span>
      <span class="brand-tagline">Protecting Africa</span>
    </span>
  </div>
  <nav class="footer-nav">
    <a href="#">HOME</a>
    <a href="#">ABOUT US</a>
    <a href="#">LINE OF BUSINESS</a>
    <a href="#">CAREER</a>
  </nav>
  <p class="copyright">© Meridane Underwriting Partners 2020, All Rights Reserved</p>
</footer>

</body>
</html>
```